Quarry IT Services Business Card

Quarry IT Services are a Perth based IT Services company. We would like to incorporate our company logo (attached) and stick with the blue that is in that design. I would like a clean look design that isn't too busy, yet creates a lasting image that is instantly recognisable in the recipients mind.

Target Market(s)

The target audience is small/medium business owners.

Industry/Entity Type

Business

Font styles to use
Serif
Sans Serif

Colors

Designer to choose colors to be used in the design.

Requirements
Must have
• The design should include:
Business name: Quarry IT Services
Directors Name: Darren Mowley
Phone Number: 0462 830 514
Email: support@quarryit.com.au
Website: www.quarryit.com.au

```html
<!DOCTYPE html>
<html lang="en">
<head>
<meta charset="utf-8">
<title>Quarry IT Services – Business Card</title>
<link href="https://fonts.googleapis.com/css2?family=Lato:wght@400;700;900&display=swap" rel="stylesheet">
<style>
  :root {
    --backdrop: #2a2a2a;
    --card-light: #f4f4f4;
    --card-mid: #dcdcdc;
    --brand-blue: #2fb1e3;
    --brand-blue-deep: #1d9fd4;
    --navy: #0c2340;
    --ink: #2b2b2b;
    --muted-blue: #cfe3ee;
    --contact-ink: #333333;
  }
  * { box-sizing: border-box; margin: 0; padding: 0; }
  html, body {
    width: 1200px; height: 900px; overflow: hidden;
    background: var(--backdrop);
    font-family: "Lato", Arial, sans-serif;
  }
  .sheet {
    position: relative; width: 1200px; height: 900px;
    display: flex; flex-direction: column; align-items: center;
    justify-content: center; gap: 50px;
  }
  .card {
    position: relative; width: 630px; height: 360px; overflow: hidden;
    background: linear-gradient(135deg, var(--card-light) 0%, #ffffff 45%, var(--card-mid) 100%);
    box-shadow: 0 14px 30px rgba(0,0,0,.55);
  }
  /* Back side */
  .card--back {
    display: flex; align-items: center; justify-content: center;
  }
  .tagline {
    font-weight: 900; font-size: 34px; line-height: 1.25;
    color: var(--ink); text-align: center; text-transform: uppercase;
    letter-spacing: .5px;
  }
  /* Front side */
  .name-tag {
    position: absolute; left: 0; top: 118px;
    background: var(--brand-blue); color: #fff;
    font-weight: 900; font-size: 23px; text-transform: uppercase;
    padding: 6px 30px 6px 26px; border-radius: 0 22px 22px 0;
  }
  .brand {
    position: absolute; right: 40px; top: 58px;
    display: flex; align-items: center; gap: 12px;
  }
  .brand__mark { width: 26px; height: 26px; background: var(--brand-blue-deep); }
  .brand__name {
    font-weight: 900; font-size: 30px; color: var(--navy);
    text-transform: uppercase; letter-spacing: .5px;
  }
  .web {
    position: absolute; right: 40px; top: 168px;
    display: flex; align-items: center; gap: 6px;
    font-weight: 700; font-size: 15px; color: var(--navy);
  }
  .band {
    position: absolute; left: 0; right: 0; top: 192px; height: 128px;
    background: linear-gradient(180deg, var(--brand-blue-deep), var(--brand-blue));
  }
  .band__company {
    position: absolute; right: 40px; top: 10px;
    font-weight: 900; font-size: 22px; color: var(--muted-blue);
    text-transform: uppercase;
  }
  .band__claim {
    position: absolute; right: 40px; top: 40px;
    font-weight: 900; font-size: 19px; color: var(--navy);
    text-transform: uppercase;
  }
  .band__email {
    position: absolute; right: 40px; bottom: 12px;
    display: flex; align-items: center; gap: 10px;
    font-size: 16px; color: var(--contact-ink);
  }
  .phone {
    position: absolute; left: 40px; bottom: 12px;
    display: flex; align-items: center; gap: 10px;
    font-size: 17px; color: var(--contact-ink); letter-spacing: 1px;
  }
</style>
</head>
<body>
<main class="sheet">
  <section class="card card--back" aria-label="Card back">
    <p class="tagline">Are you worried<br>about your technology<br>reliability ?</p>
  </section>

  <section class="card card--front" aria-label="Card front">
    <div class="name-tag">Darren Mowley</div>

    <div class="brand">
      <span class="brand__mark"></span>
      <span class="brand__name">Quarry IT Services</span>
    </div>

    <div class="web">
      <svg width="13" height="13" viewBox="0 0 16 16" aria-hidden="true">
        <g fill="none" stroke="#0c2340" stroke-width="2" stroke-linecap="round">
          <path d="M7 9.5l-1.5 1.5a2.5 2.5 0 0 1-3.5-3.5L4.5 5A2.5 2.5 0 0 1 8 5"/>
          <path d="M9 6.5l1.5-1.5A2.5 2.5 0 0 1 14 8.5L11.5 11A2.5 2.5 0 0 1 8 11"/>
        </g>
      </svg>
      <span>www.quarryit.com.au</span>
    </div>

    <div class="band">
      <p class="band__company">Quarry IT Services</p>
      <p class="band__claim">12 Years Experience in the IT Industry</p>
      <p class="band__email">
        <svg width="20" height="14" viewBox="0 0 20 14" aria-hidden="true">
          <rect x="1" y="1" width="18" height="12" fill="none" stroke="#222" stroke-width="1.6"/>
          <path d="M1 1l9 7 9-7" fill="none" stroke="#222" stroke-width="1.6"/>
        </svg>
        <span>support@quarryit.com.au</span>
      </p>
    </div>

    <p class="phone">
      <svg width="18" height="16" viewBox="0 0 18 16" aria-hidden="true">
        <path d="M1 5c0-2 3-4 8-4s8 2 8 4v1h-4V4H5v2H1z" fill="#222"/>
        <path d="M4 8l2-2h6l2 2v6H4z" fill="#222"/>
        <circle cx="9" cy="10.5" r="1.8" fill="#fff"/>
      </svg>
      <span>0462 830 514</span>
    </p>
  </section>
</main>
</body>
</html>
```